Natural, organic, vegan-friendly nutritious food supplements

We need packaging design for a new nutritious food supplement to be launched. The products are organic, natural, with no additives, lactose-free, gluten-free, vegan-friendly, etc. The product is a powder that comes in 40g sachets (need sachet design) which are then put into a box (need box design).

More details in the included zip file. Please do not hesitate to contact us for more information if needed.

Target Market(s)

Everyone interested in healthy food.

Requirements
Must have
• Vibrant colours, must be easy to read and easy to recognise on a shelf.
Natural colours.

```html
<!DOCTYPE html>
<html lang="en">
<head>
<meta charset="utf-8">
<title>VERDA Protein Powder Meal – Box and Sachet</title>
<link rel="stylesheet" href="https://fonts.googleapis.com/css2?family=Montserrat:wght@400;700;800&family=Varela+Round&family=Patrick+Hand&display=swap">
<style>
  :root {
    --teal: #68adb5;
    --teal-light: #82bcc3;
    --teal-deep: #3f7b83;
    --teal-edge: #4d8d96;
    --brown: #4f3b30;
    --brown-dark: #3a2b23;
    --cream: #ffffff;
    --lime: #e2ee5c;
    --mist: #b2e2e6;
    --name-grey: #c9c9c9;
    --ink: #2d2a27;
  }
  * { margin: 0; padding: 0; box-sizing: border-box; }
  html, body { width: 1200px; height: 1200px; overflow: hidden; background: #ffffff; }
  body { position: relative; font-family: "Montserrat", sans-serif; }

  .brand-word {
    position: absolute; left: 50%; transform: translateX(-50%);
    display: flex; align-items: center; gap: 10px;
    font-family: "Montserrat", sans-serif; font-weight: 700;
    color: var(--cream); letter-spacing: 4px; white-space: nowrap;
    line-height: 1;
  }
  .brand-dot { width: 11px; height: 11px; border-radius: 50%; background: var(--cream); display: inline-block; }

  /* ---------- Retail box ---------- */
  .retail-box { position: absolute; left: 204px; top: 146px; width: 374px; height: 837px; }
  .box-arch {
    position: absolute; left: 75px; top: 0; width: 224px; height: 224px; border-radius: 50%;
    background: var(--teal-light);
  }
  .box-header {
    position: absolute; left: 0; top: 74px; width: 374px; height: 255px;
    background: linear-gradient(180deg, var(--teal-light), var(--teal));
  }
  .retail-box .header-brand { top: 102px; font-size: 36px; }
  .box-title {
    position: absolute; left: 0; right: 0; top: 157px; text-align: center;
    color: var(--cream); font-weight: 800; font-size: 23px; line-height: 28px; letter-spacing: 1px;
  }
  .box-claims {
    position: absolute; left: 0; right: 0; top: 187px; text-align: center;
    color: var(--lime); font-family: "Varela Round", sans-serif; font-size: 10.5px; line-height: 14px; letter-spacing: .3px;
  }
  .box-tagline {
    position: absolute; left: 0; top: 220px; width: 374px; height: 35px;
    background: var(--teal-deep); color: var(--cream);
    font-weight: 700; font-size: 11.5px; letter-spacing: .5px;
    display: flex; align-items: center; justify-content: center;
  }
  .box-front {
    position: absolute; left: 0; top: 697px; width: 374px; height: 140px; z-index: 2;
    background: var(--brown); border-radius: 0 0 12px 12px;
    border-top: 2px solid var(--brown-dark);
    text-align: center;
  }
  .front-claims {
    margin-top: 14px; color: var(--mist); font-family: "Varela Round", sans-serif;
    font-size: 14.5px; line-height: 21px; letter-spacing: .4px;
  }
  .sachet-count {
    display: inline-block; margin-top: 11px; width: 136px; height: 24px; border-radius: 6px;
    background: var(--teal); color: var(--cream); font-weight: 800; font-size: 14px;
    line-height: 24px; letter-spacing: .8px;
  }
  .net-weight { margin-top: 8px; color: var(--cream); font-size: 14px; line-height: 17px; }

  /* ---------- Sachets ---------- */
  .sachet { position: absolute; overflow: hidden; background: var(--teal-edge); z-index: 1; }
  .sachet-top { position: absolute; left: 0; top: 0; width: 100%; background: var(--brown-dark); }
  .sachet-panel {
    position: absolute; left: 16px; right: 16px; top: 24px; bottom: 24px; overflow: hidden;
    background: var(--teal);
  }
  .panel-top { position: absolute; left: 0; top: 0; width: 100%; height: 135px; background: var(--brown); }
  .panel-disc {
    position: absolute; top: -2px; left: 50%; transform: translateX(-50%);
    width: 220px; height: 220px; border-radius: 50%; background: var(--brown);
  }
  .sachet .header-brand { top: 79px; font-size: 34px; }
  .sachet-kicker {
    position: absolute; left: 0; right: 0; text-align: center;
    color: var(--cream); font-size: 16px; line-height: 20px; letter-spacing: 1px;
  }
  .flavour-name {
    position: absolute; left: 0; right: 0; text-align: center;
    font-weight: 800; font-size: 34px; line-height: 44px; letter-spacing: .5px;
  }
  .flavour-name .line-one { color: var(--name-grey); display: block; }
  .flavour-name .line-two { color: var(--cream); display: block; }

  .sachet-in-box { left: 207px; top: 478px; width: 367px; height: 365px; }
  .sachet-in-box .sachet-top { height: 158px; }
  .sachet-in-box .sachet-panel { bottom: 0; }
  .sachet-in-box .sachet-kicker { top: 229px; }
  .sachet-in-box .flavour-name { top: 250px; }

  .sachet-single { left: 657px; top: 478px; width: 374px; height: 509px; }
  .sachet-single .sachet-panel { left: 17px; right: 17px; bottom: 23px; }
  .sachet-single .sachet-top { height: 160px; }
  .sachet-single .panel-top { height: 136px; }
  .sachet-single .sachet-kicker { top: 234px; }
  .sachet-single .flavour-name { top: 255px; }
  .flavour-pill {
    position: absolute; left: 56px; width: 228px; top: 350px; height: 28px; border-radius: 6px;
    background: var(--brown); color: var(--cream); text-align: center;
    font-family: "Patrick Hand", sans-serif; font-size: 22px; line-height: 28px; letter-spacing: .5px;
  }
  .sachet-claims {
    position: absolute; left: 0; right: 0; top: 389px; text-align: center;
    color: var(--mist); font-family: "Varela Round", sans-serif; font-size: 14.5px; line-height: 21px; letter-spacing: .4px;
  }
  .sachet-weight {
    position: absolute; left: 0; right: 0; top: 444px; text-align: center;
    color: var(--ink); font-size: 14px; line-height: 17px;
  }
</style>
</head>
<body>

<section class="retail-box" aria-label="Retail box of 10 sachets">
  <div class="box-arch"></div>
  <div class="box-header">
    <h2 class="box-title">PROTEIN POWDER MEAL</h2>
    <p class="box-claims">Organic &amp; Vegan | No Added Sugars | Lactose &amp; Gluten-Free</p>
    <p class="box-tagline">Positive side effects of VERDA are entirely intentional</p>
  </div>
  <div class="brand-word header-brand"><span class="brand-dot"></span>VERDA</div>
  <div class="box-front">
    <p class="front-claims">Organic &amp; Vegan | No Added Sugars<br>Lactose &amp; Gluten-Free</p>
    <span class="sachet-count">10 SACHETS</span>
    <p class="net-weight">Net Wt 40g (1.41oz) /sachet</p>
  </div>
</section>

<section class="sachet sachet-in-box" aria-label="Sachet inside box">
  <div class="sachet-top"></div>
  <div class="sachet-panel">
    <div class="panel-top"></div>
    <div class="panel-disc"></div>
    <div class="brand-word header-brand"><span class="brand-dot"></span>VERDA</div>
    <p class="sachet-kicker">PROTEIN POWDER MEAL</p>
    <h1 class="flavour-name"><span class="line-one">MERRY MOCHA</span><span class="line-two">MARVEL</span></h1>
  </div>
</section>

<section class="sachet sachet-single" aria-label="Single 40g sachet">
  <div class="sachet-top"></div>
  <div class="sachet-panel">
    <div class="panel-top"></div>
    <div class="panel-disc"></div>
    <div class="brand-word header-brand"><span class="brand-dot"></span>VERDA</div>
    <p class="sachet-kicker">PROTEIN POWDER MEAL</p>
    <h1 class="flavour-name"><span class="line-one">MERRY MOCHA</span><span class="line-two">MARVEL</span></h1>
    <p class="flavour-pill">Chocolate &amp; Coconut</p>
    <p class="sachet-claims">Organic &amp; Vegan | No Added Sugars<br>Lactose &amp; Gluten-Free</p>
    <p class="sachet-weight">Net Wt 40g (1.41oz)</p>
  </div>
</section>

</body>
</html>
```